Business Card Design - PathwayMinds

Looking for creative, modern design, two sided for PathwayMinds that is consistent with color and feel of website www.pathwayminds.example.
Updates

Back of card will be used to promote products or have a quote revolving around decisions, change, leadership, innovation, creativity. Back should also have space to promote website, but optional to use the icon. Front of the card will need to use the icon and have standard place for name, job title, phone and email. We are not looking to put a mailing address or fax. Also want space to place a few words/phrase explaining what we do...such as individual growth and organizational development or tools, training, information...in addition, want the chatterbook icon small on the front somewhere as we are also on chatterbook.

Vector file uploaded of icon.

Target Market(s)

Professional coaching for individual growth and organizational development

Industry/Entity Type

Business

Requirements
Must have
• Icon...see attached.

```html
<!DOCTYPE html>
<html lang="en">
<head>
<meta charset="utf-8">
<title>PathwayMinds – Business Card</title>
<link rel="stylesheet" href="https://fonts.googleapis.com/css2?family=Arimo:wght@400;700&family=Jost:wght@400;500&family=Open+Sans:wght@400;600&display=swap">
<style>
  :root {
    --stage: #2b2d31;
    --paper: #ffffff;
    --ink: #2a2a2a;
    --blue-deep: #0a6fc2;
    --blue-mid: #1a8fd9;
    --blue-light: #33b8ef;
    --silver: #b9c0c9;
    --white: #ffffff;
  }
  * { margin: 0; padding: 0; box-sizing: border-box; }
  html, body { width: 1200px; height: 763px; overflow: hidden; }
  body { background: var(--stage); position: relative; font-family: "Jost", sans-serif; }

  .card {
    position: absolute;
    width: 525px;
    height: 300px;
    top: 232px;
    overflow: hidden;
    box-shadow: 0 10px 28px rgba(0,0,0,.45);
  }
  .card--front { left: 50px; background: var(--paper); }
  .card--back {
    left: 625px;
    background: radial-gradient(ellipse at 50% 45%, var(--blue-light) 0%, var(--blue-mid) 40%, var(--blue-deep) 100%);
  }

  /* Front */
  .front-swoosh { position: absolute; inset: 0; }
  .brand {
    position: absolute; left: 44px; top: 34px;
    display: flex; align-items: center; gap: 18px;
  }
  .brand__mark {
    width: 78px; height: 78px; border-radius: 50%;
    background: var(--blue-mid);
  }
  .brand__name {
    font-family: "Open Sans", sans-serif; font-weight: 400;
    font-size: 30px; color: var(--ink); letter-spacing: .3px;
  }
  .tagline {
    position: absolute; left: 0; right: 0; top: 124px;
    text-align: center; font-size: 15px; color: var(--ink);
  }
  .contact {
    position: absolute; left: 0; right: 0; top: 198px;
    color: var(--white); text-align: center;
  }
  .contact__name { font-family: "Arimo", sans-serif; font-weight: 700; font-size: 20px; }
  .contact__title { font-family: "Jost", sans-serif; font-weight: 400; font-size: 17px; }
  .contact__row {
    display: flex; justify-content: center; gap: 20px;
    font-size: 14px; margin-top: 6px;
  }
  .contact__item { display: inline-flex; align-items: center; gap: 5px; }
  .icon { width: 12px; height: 12px; flex: none; }
  .social-square { width: 11px; height: 11px; background: rgba(255,255,255,.75); display: inline-block; }

  /* Back */
  .back-mark {
    position: absolute; left: 202px; top: 90px;
    width: 120px; height: 120px; border-radius: 50%;
    background: rgba(255,255,255,.1);
  }
  .quotes {
    position: relative; padding: 26px 20px 0;
    font-family: "Arimo", sans-serif; color: var(--white);
    text-align: center;
  }
  .quote { margin-bottom: 7px; }
  .quote__text { font-size: 13.5px; line-height: 1.2; }
  .quote__text::before { content: "\201C"; font-weight: 700; font-size: 17px; }
  .quote__text::after { content: "\201D"; font-weight: 700; font-size: 17px; }
  .quote__author { font-size: 13.5px; font-weight: 700; }
</style>
</head>
<body>

<section class="card card--front" aria-label="Card front">
  <svg class="front-swoosh" viewBox="0 0 525 300" preserveAspectRatio="none" aria-hidden="true">
    <defs>
      <linearGradient id="bandBlue" x1="0" y1="1" x2="1" y2="0">
        <stop offset="0" stop-color="#0a6fc2"/>
        <stop offset="1" stop-color="#33b8ef"/>
      </linearGradient>
    </defs>
    <path d="M0 238 Q210 150 525 150 L525 157 Q215 158 0 246 Z" fill="#b9c0c9"/>
    <path d="M0 250 Q220 164 525 160 L525 300 L0 300 Z" fill="url(#bandBlue)"/>
  </svg>

  <div class="brand">
    <span class="brand__mark" aria-hidden="true"></span>
    <span class="brand__name">PathwayMinds</span>
  </div>

  <p class="tagline">Helping people and teams grow through clear, confident choices.</p>

  <div class="contact">
    <p><span class="contact__name">Your Name,</span> <span class="contact__title">Title</span></p>
    <div class="contact__row">
      <span class="contact__item">
        <svg class="icon" viewBox="0 0 12 12" aria-hidden="true"><path d="M3 1 L5 3.5 L4 5 Q5.5 7 7 8 L8.5 7 L11 9 L9.5 11 Q4 10 1 2.5 Z" fill="#fff"/></svg>
        555-210-4478
      </span>
      <span class="contact__item">
        <svg class="icon" viewBox="0 0 12 12" aria-hidden="true"><rect x="1" y="3" width="10" height="7" fill="none" stroke="#fff" stroke-width="1.3"/><path d="M1 3 L6 7 L11 3" fill="none" stroke="#fff" stroke-width="1.3"/></svg>
        info@pathwayminds.example
      </span>
    </div>
    <div class="contact__row">
      <span class="contact__item">
        <svg class="icon" viewBox="0 0 12 12" aria-hidden="true"><circle cx="6" cy="6" r="5" fill="none" stroke="#fff" stroke-width="1.2"/><ellipse cx="6" cy="6" rx="2.2" ry="5" fill="none" stroke="#fff" stroke-width="1"/><line x1="1" y1="6" x2="11" y2="6" stroke="#fff" stroke-width="1"/></svg>
        www.pathwayminds.example
      </span>
      <span class="contact__item">
        <span class="social-square" aria-hidden="true"></span>
        /pathwayminds
      </span>
    </div>
  </div>
</section>

<section class="card card--back" aria-label="Card back">
  <span class="back-mark" aria-hidden="true"></span>
  <div class="quotes">
    <div class="quote"><p class="quote__text">Try not to become a man of success, but rather a man of value.</p><p class="quote__author">- Alvin Eastman</p></div>
    <div class="quote"><p class="quote__text">The only constant is change.</p><p class="quote__author">- Heron Lykos</p></div>
    <div class="quote"><p class="quote__text">We are what we repeatedly do. Excellence is not an act, it is a habit.</p><p class="quote__author">- Arion Castell</p></div>
    <div class="quote"><p class="quote__text">Simplicity is the ultimate sophistication.</p><p class="quote__author">- Leo Davenport</p></div>
    <div class="quote"><p class="quote__text">Life is not fair - get used to it.</p><p class="quote__author">- Bill Garner</p></div>
  </div>
</section>

</body>
</html>
```